practice letterhead

I need a letterhead design for a new company that is a veterinary specialty company. I am conservative. I want it to look professional - not "cutesy"

I need my name, credentials, address, phone number and website/email on it.

My personal information is as follows: Marisol Tedder, DVM, DACVIM (Neurology) Certified Veterinary Pain Practitioner (or CVPP) Certified Canine Rehabilitation Therapist (or CCRT) 4170 Larkfield Hwy Larkin Falls, MA 01964 508-347-6620 marisol.tedder@petspineandcare.com www.petspineandcare.com

```html
<!DOCTYPE html>
<html lang="en">
<head>
<meta charset="utf-8">
<title>Practice Letterhead</title>
<link href="https://fonts.googleapis.com/css2?family=Open+Sans:ital,wght@0,400;0,600;1,400;1,700&display=swap" rel="stylesheet">
<style>
  :root {
    --backdrop: #e4e4e4;
    --paper: #fbfbfb;
    --navy: #1f3a48;
    --sage: #5e8f7e;
    --ink: #3f4a4f;
    --muted: #6c7478;
    --ghost-a: #dcdcdc;
    --ghost-b: #ececec;
  }
  * { box-sizing: border-box; margin: 0; padding: 0; }
  html, body { width: 1200px; height: 968px; overflow: hidden; }
  body {
    background: var(--backdrop);
    font-family: "Open Sans", Arial, sans-serif;
    color: var(--ink);
  }
  .letterhead {
    position: absolute;
    left: 252px; top: 34px;
    width: 696px; height: 900px;
    background: var(--paper);
    box-shadow: 0 2px 10px rgba(0,0,0,0.12);
  }
  .sender { position: absolute; left: 56px; top: 48px; }
  .sender-name {
    font-size: 13px; font-weight: 700; font-style: italic;
    color: var(--sage); letter-spacing: 0.04em; text-transform: uppercase;
  }
  .sender-credentials {
    list-style: none; margin-top: 3px;
    font-size: 9.5px; font-style: italic; color: var(--muted); line-height: 1.45;
  }
  .practice-mark {
    position: absolute; right: 48px; top: 96px;
    display: flex; align-items: center; gap: 10px;
  }
  .practice-dot { width: 34px; height: 34px; border-radius: 50%; background: var(--navy); flex: none; }
  .practice-name {
    font-size: 15px; font-weight: 600; color: var(--sage); line-height: 1.2; width: 190px;
  }
  .contact {
    position: absolute; left: 56px; top: 712px;
    list-style: none; font-size: 10px; color: var(--ink); line-height: 1;
  }
  .contact li { display: flex; align-items: center; gap: 6px; margin-bottom: 6px; }
  .contact svg { width: 10px; height: 10px; flex: none; }
  .band { position: absolute; height: 9px; }
  .band-navy { left: 0; top: 792px; width: 300px; background: var(--navy); }
  .band-sage { left: 352px; top: 792px; width: 344px; background: var(--sage); }
  .hand-art {
    position: absolute; left: 300px; top: 776px; width: 52px; height: 34px;
    background: var(--navy); border-radius: 4px 18px 18px 4px;
  }
  .ghost-art {
    position: absolute; left: 330px; top: 612px; width: 110px; height: 160px;
    background: linear-gradient(180deg, var(--ghost-b), var(--ghost-a));
    border-radius: 40px 40px 10px 10px;
  }
  .address {
    position: absolute; left: 500px; top: 748px;
    font-size: 11px; color: var(--ink); line-height: 1.4; font-style: normal;
  }
</style>
</head>
<body>
  <main class="letterhead">
    <header class="sender">
      <h1 class="sender-name">Marisol Tedder</h1>
      <ul class="sender-credentials">
        <li>DVM, DACVIM (Neurology)</li>
        <li>Certified Veterinary Pain Practitioner</li>
        <li>Certified Canine Rehabilitation Therapist</li>
      </ul>
    </header>

    <div class="practice-mark">
      <span class="practice-dot"></span>
      <span class="practice-name">Larkfield Veterinary Spine &amp; Comfort Center</span>
    </div>

    <ul class="contact">
      <li>
        <svg viewBox="0 0 10 10"><circle cx="5" cy="5" r="4.4" fill="none" stroke="#3f4a4f" stroke-width="0.8"/><path d="M3.4 2.8l1 .9-.5.8c.4.8.9 1.3 1.6 1.6l.8-.5.9 1-.7.7C4.7 7.2 2.9 5.4 2.8 3.6z" fill="#3f4a4f"/></svg>
        508-347-6620
      </li>
      <li>
        <svg viewBox="0 0 10 10"><circle cx="5" cy="5" r="4.4" fill="none" stroke="#3f4a4f" stroke-width="0.8"/><rect x="2.8" y="3.4" width="4.4" height="3.2" fill="none" stroke="#3f4a4f" stroke-width="0.6"/><path d="M2.8 3.4L5 5.2l2.2-1.8" fill="none" stroke="#3f4a4f" stroke-width="0.6"/></svg>
        marisol.tedder@petspineandcare.com
      </li>
      <li>
        <svg viewBox="0 0 10 10"><circle cx="5" cy="5" r="4.4" fill="none" stroke="#3f4a4f" stroke-width="0.8"/><ellipse cx="5" cy="5" rx="1.6" ry="3.2" fill="none" stroke="#3f4a4f" stroke-width="0.6"/><path d="M1.8 5h6.4" stroke="#3f4a4f" stroke-width="0.6"/></svg>
        www.petspineandcare.com
      </li>
    </ul>

    <div class="ghost-art" role="img" aria-label="Faint silhouette of a person with a dog"></div>
    <div class="band band-navy"></div>
    <div class="hand-art" role="img" aria-label="Open hand illustration"></div>
    <div class="band band-sage"></div>

    <address class="address">
      4170 Larkfield Hwy<br>
      Larkin Falls, MA 01964
    </address>
  </main>
</body>
</html>
```